Bramblewood Craft Spirits Bottle Label

Bramblewood Craft Spirits is a distillery and craft cocktail bar that will be located in Calgary, Alberta, Canada. Here, we create awesome hand crafted spirits like vodka, gin, rum, whiskey, brandy, liqueurs etc. We need bottle labels for 3 different initial products. The names of the products are as follows, Orchard Dash Gin (22% alc/vol), Toverin Dry Gin (40% alc/vol), and Palundro Contemporary Gin (40% alc/vol). It would be preferable to have 3 distinct labels. The alcohol by volume declaration must be on the front display of the label, without having to turn the bottle. There is a logo for Bramblewood Craft Spirits I would like featured in the front around 1''x1" or 2.5cm x 2.5cm in size. Some last minute changes are being made to the logo so it is not uploaded at this moment. Abstract geometry would be a great fit for the contemporary gin and I have attached an example.Simple or complex designs both encouraged. The Orchard Dash Gin will be in the Moonea style bottle and the other two will be in Apotheker style bottles. Thank you so much to anyone interested in participating and we can't wait to hear from you. This is a great opportunity to showcase your creativity and be involved with future products!
Young professionals ages 21-30.

```html
<!DOCTYPE html>
<html lang="en">
<head>
<meta charset="utf-8">
<title>Bramblewood Craft Spirits – Gin Labels</title>
<link rel="stylesheet" href="https://fonts.googleapis.com/css2?family=Cinzel:wght@400;600&family=Cinzel+Decorative:wght@700&family=Lobster&family=Montserrat:wght@800&family=Great+Vibes&family=Crimson+Text&display=swap">
<style>
  :root {
    --page: #ffffff;
    --orchard-border: #2f6b2a;
    --orchard-frame: #8cc63f;
    --orchard-light: #eef7d8;
    --orchard-mid: #b9dc86;
    --orchard-ink: #2d5a26;
    --toverin-border: #2b3a8f;
    --toverin-frame: #b3c1d4;
    --toverin-deep: #0b1a4a;
    --toverin-mid: #1f49a6;
    --toverin-ink: #ffffff;
    --palundro-border: #d52a1e;
    --palundro-frame: #e97a22;
    --palundro-red: #d8291f;
    --palundro-orange: #ef7b22;
    --palundro-yellow: #f7d531;
    --palundro-plum: #8c3a5a;
    --palundro-ink: #ffffff;
  }
  * { margin: 0; padding: 0; box-sizing: border-box; }
  html, body { width: 1200px; height: 1028px; overflow: hidden; background: var(--page); }
  .canvas { position: relative; width: 1200px; height: 1028px; }

  .label {
    position: absolute; top: 462px; width: 244px; height: 262px;
    border: 3px solid; padding: 8px;
  }
  .label__panel {
    position: relative; width: 100%; height: 100%;
    border-radius: 10px; text-align: center; overflow: hidden;
  }
  .label__brand {
    position: absolute; top: 14px; left: 0; right: 0;
    font-family: "Cinzel", serif; font-weight: 600; font-size: 8.5px; letter-spacing: 0.3px;
  }
  .label__kind {
    position: absolute; top: 158px; left: 0; right: 0;
    font-family: "Cinzel", serif; font-size: 27px; letter-spacing: 16px; padding-left: 16px;
  }
  .label__abv {
    position: absolute; top: 199px; left: 0; right: 0;
    font-family: "Crimson Text", serif; font-size: 13px;
  }
  .label__rule {
    position: absolute; top: 222px; left: 50%; width: 110px; margin-left: -55px;
    height: 1px; background: currentColor;
  }

  /* Orchard Dash */
  .label--orchard { left: 123px; border-color: var(--orchard-border); background: var(--orchard-frame); }
  .label--orchard .label__panel {
    background: linear-gradient(140deg, var(--orchard-mid) 0%, var(--orchard-light) 45%, var(--orchard-light) 70%, var(--orchard-mid) 100%);
    color: var(--orchard-ink);
  }
  .orchard-title { position: absolute; top: 38px; left: 0; right: 0; font-family: "Lobster", cursive; color: var(--orchard-ink); line-height: 0.95; }
  .orchard-title__first { display: block; font-size: 40px; text-align: left; padding-left: 14px; }
  .orchard-title__second { display: block; font-size: 40px; text-align: right; padding-right: 22px; }
  .label--orchard .label__kind { color: #4a5a44; }
  .label--orchard .label__abv { color: #333; }

  /* Toverin Dry */
  .label--toverin { left: 466px; border-color: var(--toverin-border); background: var(--toverin-frame); }
  .label--toverin .label__panel {
    background: radial-gradient(ellipse at 50% 45%, var(--toverin-mid) 0%, var(--toverin-deep) 85%);
    color: var(--toverin-ink);
  }
  .toverin-title { position: absolute; top: 52px; left: 0; right: 0; font-family: "Cinzel Decorative", serif; font-weight: 700; line-height: 0.9; }
  .toverin-title__first { display: block; font-size: 30px; }
  .toverin-title__second { display: block; font-size: 36px; }

  /* Palundro Contemporary */
  .label--palundro { left: 814px; border-color: var(--palundro-border); background: var(--palundro-frame); }
  .label--palundro .label__panel {
    background: linear-gradient(150deg, var(--palundro-orange) 0%, var(--palundro-red) 35%, var(--palundro-red) 60%, var(--palundro-orange) 78%, var(--palundro-yellow) 92%, var(--palundro-plum) 100%);
    color: var(--palundro-ink);
  }
  .palundro-title { position: absolute; top: 58px; left: 0; right: 0; }
  .palundro-title__name { display: block; font-family: "Montserrat", sans-serif; font-weight: 800; font-size: 30px; letter-spacing: -0.5px; }
  .palundro-title__style { display: block; font-family: "Great Vibes", cursive; font-size: 26px; margin-top: -4px; }
</style>
</head>
<body>
<main class="canvas">

  <section class="label label--orchard" aria-label="Orchard Dash Gin label">
    <div class="label__panel">
      <p class="label__brand">Bramblewood Craft Spirits</p>
      <h2 class="orchard-title">
        <span class="orchard-title__first">Orchard</span>
        <span class="orchard-title__second">Dash</span>
      </h2>
      <p class="label__kind">GIN</p>
      <p class="label__abv">22% alc / vol</p>
      <span class="label__rule"></span>
    </div>
  </section>

  <section class="label label--toverin" aria-label="Toverin Dry Gin label">
    <div class="label__panel">
      <p class="label__brand">Bramblewood Craft Spirits</p>
      <h2 class="toverin-title">
        <span class="toverin-title__first">TOVERIN</span>
        <span class="toverin-title__second">DRY</span>
      </h2>
      <p class="label__kind">GIN</p>
      <p class="label__abv">40% alc / vol</p>
      <span class="label__rule"></span>
    </div>
  </section>

  <section class="label label--palundro" aria-label="Palundro Contemporary Gin label">
    <div class="label__panel" role="img" aria-label="Diagonal stripes in red, orange and yellow behind the label text">
      <p class="label__brand">Bramblewood Craft Spirits</p>
      <h2 class="palundro-title">
        <span class="palundro-title__name">PALUNDRO</span>
        <span class="palundro-title__style">Contemporary</span>
      </h2>
      <p class="label__kind">GIN</p>
      <p class="label__abv">40% alc / vol</p>
      <span class="label__rule"></span>
    </div>
  </section>

</main>
</body>
</html>
```